Flower delivery business needs sales brochure

I have a courier business that specialises in same-day flower deliveries; I want to make a single page A4 sales brochure (folded to DL) to give to our potential customers.
The company website is petalvanto.com, this will give an idea of who we are and what we do, as well as some graphics and colours that we use.
When opened, the inside A4 space of the brochure will be a pricelist, so the entire page will be an excel table with delivery locations and prices; we will add the prices ourselves later, so ideally the inside will be a background of some sort that won't obstruct text. Maybe light/transparent flowers and a background colour?
The front of the DL brochure should be mostly a title page, so business name, phone number, a graphic?
The first inside page should relate to our service, there's a lot of info on our website that you could use, so same day delivery, 10:30 and 2:30 pick-up times, established over 10 years ago, air-conditioned vans, delivery to 300+ suburbs.
The back page would be contact details and maybe a summary of the key points of the 'about us' section of the website.

Industry/Entity Type

Business

```html
<!DOCTYPE html>
<html lang="en">
<head>
<meta charset="utf-8">
<title>Petal Vanto – Florist Delivery Brochure</title>
<link rel="stylesheet" href="https://fonts.googleapis.com/css2?family=Cinzel:wght@700&family=Kalam:wght@700&family=Hind:wght@400;500&display=swap">
<style>
  :root {
    --page-bg: #e9e6e1;
    --green-light: #6aa823;
    --green-dark: #2f6a10;
    --green-ink: #234a12;
    --green-text: #3f7c1c;
    --orange: #e8561c;
    --orange-light: #f27a2e;
    --red: #c63a1c;
    --board: #eeeced;
    --board-line: #dcdadb;
    --white: #ffffff;
  }
  * { box-sizing: border-box; margin: 0; padding: 0; }
  html, body { width: 1200px; height: 900px; overflow: hidden; }
  body { background: var(--page-bg); font-family: "Hind", Arial, sans-serif; position: relative; }

  .brochure {
    position: absolute; left: 60px; top: 70px;
    width: 1080px; height: 760px; overflow: hidden;
    background: var(--board);
    box-shadow: 0 6px 24px rgba(0,0,0,.18);
  }
  .brochure-art { position: absolute; inset: 0; }

  .about-title {
    position: absolute; left: 0; width: 360px; top: 398px;
    text-align: center; font-family: "Kalam", cursive; font-weight: 700;
    font-size: 30px; color: #1d2a10;
  }
  .about-text {
    position: absolute; left: 56px; top: 446px; width: 292px;
    color: var(--white); font-size: 14.5px; line-height: 19.5px;
  }
  .about-text p + p { margin-top: 2px; }
  .about-web {
    position: absolute; left: 56px; top: 697px;
    color: var(--white); font-size: 22px; font-weight: 500;
  }

  .contact { position: absolute; left: 360px; width: 360px; top: 222px; text-align: center; }
  .contact-call { font-family: "Cinzel", serif; font-weight: 700; font-size: 29px; color: var(--red); letter-spacing: .5px; }
  .contact-phone { font-size: 32px; color: var(--green-ink); font-weight: 500; margin-top: -2px; letter-spacing: 1px; }
  .contact-email { font-size: 17px; color: var(--green-ink); font-weight: 500; display: flex; justify-content: center; align-items: center; gap: 8px; margin-top: 0; }
  .contact-web { font-size: 21px; color: var(--green-text); font-weight: 500; margin-top: 0; }

  .brand {
    position: absolute; left: 745px; top: 38px; display: flex; align-items: center; gap: 10px;
  }
  .brand-dot { width: 40px; height: 40px; border-radius: 50%; background: var(--orange); }
  .brand-name {
    font-family: "Kalam", cursive; font-weight: 700; font-size: 29px;
    color: var(--green-dark); text-transform: uppercase; letter-spacing: 1px;
  }
  .headline {
    position: absolute; left: 720px; width: 360px; top: 118px; text-align: center;
    font-family: "Kalam", cursive; font-weight: 700; font-size: 36px; line-height: 47px;
    color: #2b4d14;
  }
</style>
</head>
<body>
  <main class="brochure">
    <svg class="brochure-art" width="1080" height="760" viewBox="0 0 1080 760" aria-hidden="false">
      <defs>
        <linearGradient id="greenPanel" x1="0" y1="0" x2="0" y2="1">
          <stop offset="0" stop-color="var(--green-light)"/>
          <stop offset="1" stop-color="var(--green-dark)"/>
        </linearGradient>
        <linearGradient id="orangeBand" x1="0" y1="0" x2="1" y2="0">
          <stop offset="0" stop-color="var(--orange)"/>
          <stop offset="1" stop-color="var(--orange-light)"/>
        </linearGradient>
        <linearGradient id="poppyWash" x1="0" y1="0" x2="0" y2="1">
          <stop offset="0" stop-color="#f7f3ee"/>
          <stop offset=".55" stop-color="#f6e3e6"/>
          <stop offset="1" stop-color="#eec4cf"/>
        </linearGradient>
        <radialGradient id="shopPhoto" cx=".5" cy=".45" r=".6">
          <stop offset="0" stop-color="#e6e0d3"/>
          <stop offset=".6" stop-color="#c9c9a2"/>
          <stop offset="1" stop-color="#8f9a5a"/>
        </radialGradient>
        <radialGradient id="tulipPhoto" cx=".5" cy=".55" r=".55">
          <stop offset="0" stop-color="#f6d31c"/>
          <stop offset=".55" stop-color="#efd560"/>
          <stop offset="1" stop-color="#eeecec"/>
        </radialGradient>
        <radialGradient id="gardenPhoto" cx=".45" cy=".4" r=".6">
          <stop offset="0" stop-color="#e8a0b8"/>
          <stop offset=".35" stop-color="#6f9f3a"/>
          <stop offset="1" stop-color="#2f6b1c"/>
        </radialGradient>
        <pattern id="boards" width="360" height="44" patternUnits="userSpaceOnUse">
          <rect width="360" height="44" fill="var(--board)"/>
          <rect y="42" width="360" height="2" fill="var(--board-line)"/>
        </pattern>
      </defs>

      <!-- middle panel boards -->
      <rect x="360" y="0" width="360" height="760" fill="url(#boards)"/>

      <!-- right panel background -->
      <g role="img" aria-label="Soft pink poppy flowers on a cream background">
        <rect x="720" y="0" width="360" height="760" fill="url(#poppyWash)"/>
      </g>

      <!-- left green panel -->
      <rect x="0" y="0" width="360" height="760" fill="url(#greenPanel)"/>

      <!-- top-left shop photo in circle -->
      <circle cx="205" cy="150" r="228" fill="var(--orange)"/>
      <circle cx="205" cy="150" r="220" fill="var(--white)"/>
      <g role="img" aria-label="Smiling florist in an apron holding a tablet among potted yellow daffodils">
        <circle cx="205" cy="150" r="210" fill="url(#shopPhoto)"/>
      </g>

      <!-- yellow tulips -->
      <g role="img" aria-label="Bunch of yellow tulips lying on white wooden boards">
        <ellipse cx="500" cy="570" rx="140" ry="130" fill="url(#tulipPhoto)"/>
      </g>

      <!-- orange bottom band with curve -->
      <path d="M0 660 L360 660 C470 660 560 640 690 625 L705 760 L0 760 Z" fill="url(#orangeBand)"/>
      <path d="M0 660 L360 660 L360 760 L0 760 Z" fill="var(--orange)" opacity=".35"/>

      <!-- big garden photo circle -->
      <circle cx="905" cy="625" r="280" fill="var(--green-dark)"/>
      <circle cx="905" cy="625" r="268" fill="var(--white)"/>
      <g role="img" aria-label="Little girl in pink holding a large bouquet of pink peonies in a green garden">
        <circle cx="905" cy="625" r="262" fill="url(#gardenPhoto)"/>
      </g>
    </svg>

    <h2 class="about-title">ABOUT US:</h2>
    <div class="about-text">
      <p>Petal Vanto Pty Ltd is a courier company that specializes in the delivery of flowers and gifts.</p>
      <p>We offer a same day courier service for the florist &amp; gift retail and wholesale market, and deliver to over 300 suburbs throughout the Brisbane Metropolitan region</p>
      <p>We have been in the business for over 10 years, and are very focused on delivering the best customer service possible.</p>
    </div>
    <div class="about-web">www.petalvanto.com</div>

    <section class="contact">
      <div class="contact-call">CALL US:</div>
      <div class="contact-phone">0400 555 012</div>
      <div class="contact-email">
        <svg width="26" height="17" viewBox="0 0 26 17" aria-hidden="true">
          <rect x="1" y="1" width="24" height="15" fill="var(--green-text)"/>
          <path d="M1 1 L13 10 L25 1" fill="none" stroke="var(--white)" stroke-width="1.6"/>
        </svg>
        <span>info@petalvanto.com</span>
      </div>
      <div class="contact-web">www.petalvanto.com</div>
    </section>

    <div class="brand">
      <span class="brand-dot"></span>
      <span class="brand-name">Petal Vanto</span>
    </div>
    <h1 class="headline">We<br>Deliver Stylish,<br>fresh flowers</h1>
  </main>
</body>
</html>
```